medical equipment home page redesign

We need a new home page for an existing store. We'll be redoing the entire site to make it more user friendly and follow talequill guidelines. We have a loose wireframe for the sections, but need help making it look great. The look should be clean, modern, professional, etc. We have a background image we would like to incorporate somewhere because we've just printed business cards and brochures that use this background image. We love parallax effects on backgrounds, so please allow extra big background images so we can utilize that effect. You can find images, etc from our site at brivolune.com. We like the way this site feels: http://tkro.palvenix.com/home/page/venue with the parallax background. And this one, too: https://www.muddersheriot.org/

Target Market(s)

people with chronic pain

Industry/Entity Type

Medical Equipment

Number of Pages Required

1 page

Font styles to use
Sans Serif

Colors
b8a6cd
6b449b
e4daeb

Requirements
Must have
• Please include sections from our wireframe. They don't have to look like the wireframe, but they do need to portray that information in each section.
Nice to have
• It would be great if you could include the background image we have attached
Should not have
• Should not look like the old site.

```html
<!DOCTYPE html>
<html lang="en">
<head>
<meta charset="utf-8">
<title>Brivolune — Light Your Way Out of Pain</title>
<link href="https://fonts.googleapis.com/css2?family=Montserrat:wght@400;500;600;700&display=swap" rel="stylesheet">
<style>
:root{
  --purple:#6b449b;
  --lilac:#b8a6cd;
  --mist:#e4daeb;
  --ink:#222222;
  --grey:#777777;
  --white:#ffffff;
}
*{box-sizing:border-box;margin:0;padding:0}
html,body{width:1200px;height:3519px;overflow:hidden}
body{position:relative;font-family:'Montserrat',sans-serif;color:var(--ink);background:var(--white)}
.abs{position:absolute}
.brand{display:flex;align-items:center;gap:8px;font-weight:700;color:var(--purple)}
.brand .dot{width:14px;height:14px;border-radius:50%;background:var(--purple)}
.site-header{left:0;top:0;width:1200px;height:62px;background:var(--white)}
.site-header .brand{position:absolute;left:200px;top:18px;font-size:22px}
.nav{position:absolute;top:24px;font-size:10px;color:#333}
.nav.active{color:var(--purple)}
.btn{background:var(--purple);color:var(--white);font-size:10px;font-weight:600;display:flex;align-items:center;justify-content:center;letter-spacing:.3px}
.hero{left:0;top:62px;width:1200px;height:364px;background:linear-gradient(180deg,#e9e3e6 0%,#ece4e8 45%,#e2d6df 75%,#d7cad6 100%)}
.hero h1{position:absolute;left:200px;top:95px;font-size:30px;font-weight:600}
.hero p{position:absolute;left:200px;top:143px;font-size:13px;font-weight:500}
.hero-products{left:629px;top:137px;width:370px;height:171px;border-radius:6px;background:linear-gradient(120deg,#6c6c70,#9a9aa0 45%,#c7c7cc)}
.feature{top:372px;width:256px;height:113px;background:var(--purple);color:var(--white);display:flex;flex-direction:column;align-items:center;justify-content:center;gap:10px;font-size:15px;font-weight:500}
.section-title{position:absolute;left:0;width:1200px;text-align:center;font-size:20px;font-weight:500}
.rule{position:absolute;left:570px;width:60px;height:2px;background:var(--purple)}
.rule.light{background:var(--white)}
.therapy-img{top:616px;width:194px;height:171px}
.therapy-label{top:809px;width:194px;text-align:center;font-size:15px;font-weight:500}
.see-more{position:absolute;left:43px;top:70px;width:109px;height:31px;border:2px solid var(--white);color:var(--white);font-size:9px;font-weight:600;display:flex;align-items:center;justify-content:center}
.trust-band{left:0;top:873px;width:1200px;height:312px;background:linear-gradient(100deg,#f7e4b0 0%,#f0c58d 25%,#e7b39a 55%,#c9b2bd 80%,#aab6c4 100%)}
.testimonial{top:975px;width:357px;height:266px;background:var(--white);box-shadow:0 1px 6px rgba(0,0,0,.12);text-align:center}
.avatar{position:absolute;left:147px;top:-14px;width:63px;height:63px;border-radius:50%;background:#9b8f88;border:3px solid var(--white)}
.testimonial .name{position:absolute;top:63px;width:100%;color:var(--purple);font-size:13px;font-weight:500}
.testimonial .role{position:absolute;top:80px;width:100%;color:#aaa;font-size:8px}
.testimonial .quote{position:absolute;top:104px;width:100%;color:var(--purple);font-size:32px;font-weight:700;line-height:1}
.testimonial .text{position:absolute;top:144px;left:20px;right:20px;font-size:8.5px;line-height:22px;color:#555}
.arrow{font-size:18px;color:var(--white)}
.card{background:var(--white);box-shadow:0 1px 5px rgba(0,0,0,.15)}
.audience{top:1360px;width:256px;height:302px}
.card .photo{width:100%;height:119px}
.card h3{position:absolute;left:12px;font-size:13px;font-weight:600}
.card .body{position:absolute;left:12px;right:12px;font-size:9px;line-height:19px;color:#444}
.read-more{position:absolute;left:14px;font-size:10px;font-weight:500;color:var(--purple);border-bottom:1px solid var(--purple);padding-bottom:2px}
.featured-band{left:0;top:1707px;width:1200px;height:358px;background:linear-gradient(100deg,#c1afd6 0%,#b29ed0 50%,#7d56aa 100%)}
.product{top:1811px;width:175px;height:193px;background:var(--white)}
.product .photo{height:116px;background:linear-gradient(135deg,#3d3d42,#9a9aa0 60%,#e4b8d3)}
.product .pname{position:absolute;left:7px;top:126px;font-size:10px;font-weight:500;line-height:12px}
.product .price{position:absolute;left:7px;font-size:8px;color:var(--purple)}
.product .view{position:absolute;left:7px;top:174px;font-size:8px;font-weight:500;color:var(--purple)}
.dots{left:580px;top:2030px;display:flex;gap:6px}
.dots span{width:8px;height:8px;border-radius:50%;background:var(--white);opacity:.6}
.dots span:first-child{opacity:1}
.video{left:353px;top:2220px;width:490px;height:278px;border-radius:4px;background:linear-gradient(90deg,#5f3fa3 0%,#b94a4a 45%,#3a9bd0 65%,#8b2b2b 100%)}
.play{position:absolute;left:228px;top:126px;width:34px;height:24px;border-radius:5px;background:rgba(0,0,0,.75);display:flex;align-items:center;justify-content:center}
.blog-band{left:0;top:2601px;width:1200px;height:373px;background:linear-gradient(180deg,#e6dfe3 0%,#ece5e9 50%,#dccfda 100%)}
.post{top:2706px;width:256px;height:314px}
.post h3{font-size:10.5px;text-transform:uppercase}
.post .date{position:absolute;left:12px;top:152px;font-size:8px;color:#555}
.signup-field{left:440px;width:321px;font-size:10px;border-bottom:1px solid var(--purple);padding-bottom:4px}
.footer{left:0;top:3368px;width:1200px;height:151px;background:linear-gradient(100deg,#b8a6cd 0%,#a48cc4 55%,#6b449b 100%);color:var(--white)}
.footer .brand{position:absolute;left:200px;top:36px;font-size:24px;color:var(--white)}
.footer .brand .dot{background:var(--white)}
.footer small{position:absolute;font-size:9.5px}
.links{position:absolute;left:663px;top:37px;font-size:9.5px;line-height:18.5px}
</style>
</head>
<body>

<header class="abs site-header">
  <div class="brand"><span class="dot"></span>Brivolune</div>
  <span class="nav active" style="left:664px">Home</span>
  <span class="nav" style="left:729px">What's New?</span>
  <span class="nav" style="left:826px">About us</span>
  <span class="abs btn" style="left:902px;top:18px;width:98px;height:28px;font-size:9px">SHOP NOW</span>
</header>

<section class="abs hero">
  <h1>Light Your Way Out of Pain</h1>
  <p>Because everyone deserves acess to a pain free life</p>
  <span class="abs btn" style="left:200px;top:187px;width:131px;height:34px;font-size:11px">SHOP NOW</span>
</section>
<div class="abs hero-products" role="img" aria-label="Four handheld therapy lights in grey, red, blue and green"></div>

<div class="abs feature" style="left:200px">
  <svg width="38" height="38" viewBox="0 0 38 38" fill="none" stroke="#fff" stroke-width="3"><circle cx="19" cy="19" r="16"/><line x1="8" y1="8" x2="30" y2="30"/></svg>
  Drug Free
</div>
<div class="abs feature" style="left:471px">
  <svg width="34" height="34" viewBox="0 0 34 34" fill="none" stroke="#fff" stroke-width="2.5"><circle cx="17" cy="17" r="14"/><circle cx="12" cy="13" r="1" fill="#fff"/><circle cx="22" cy="13" r="1" fill="#fff"/><path d="M10 20q7 7 14 0"/></svg>
  Safe
</div>
<div class="abs feature" style="left:743px">
  <svg width="38" height="38" viewBox="0 0 38 38" fill="none" stroke="#fff" stroke-width="2.5"><path d="M26 4l8 8M30 8l-4 4M24 10l4 4L14 28l-6 2 2-6z"/><line x1="8" y1="30" x2="3" y2="35"/><path d="M18 16l3 3M15 19l3 3"/></svg>
  Pain Relief
</div>

<h2 class="section-title" style="top:536px">How Light Therapy Can Stop Your Pain</h2>
<div class="rule" style="top:582px"></div>

<div class="abs therapy-img" style="left:200px;background:linear-gradient(180deg,#8a5aa8,#b074b8);" role="img" aria-label="Photobiomodulation light head with LEDs">
  <span class="see-more">SEE MORE</span>
</div>
<div class="abs therapy-img" style="left:402px;background:radial-gradient(circle at 55% 40%,#ff3d8a,#b0124e 60%,#3a0a1a)" role="img" aria-label="Red light applied to a person"></div>
<div class="abs therapy-img" style="left:604px;background:radial-gradient(circle at 50% 60%,#5be08a,#2a7a4a 55%,#1c2a1f)" role="img" aria-label="Green light shining through a glass of water"></div>
<div class="abs therapy-img" style="left:806px;background:linear-gradient(135deg,#7e84b8,#c9bfb6 50%,#8e8078)" role="img" aria-label="Blue light used on a cat"></div>
<span class="abs therapy-label" style="left:200px">PBM</span>
<span class="abs therapy-label" style="left:402px">Red</span>
<span class="abs therapy-label" style="left:604px">Green</span>
<span class="abs therapy-label" style="left:806px">Blue</span>

<section class="abs trust-band" role="img" aria-label="Sunset sky background">
</section>
<h2 class="section-title" style="top:894px">They Trusted Us</h2>
<div class="rule" style="top:938px"></div>
<span class="abs arrow" style="left:199px;top:1088px">&#8249;</span>
<span class="abs arrow" style="left:992px;top:1093px">&#8250;</span>

<article class="abs testimonial" style="left:231px">
  <div class="avatar" role="img" aria-label="Customer portrait"></div>
  <div class="name">John Doe</div>
  <div class="role">CEO of doeview.com</div>
  <div class="quote">&#8221;</div>
  <p class="text">Lorem ipsum dolor sit amet, consectetur adipiscing elit, sed do eiusmod tempor incididunt ut labore et dolore magna aliqua. Quis ipsum suspendisse ultrices gravida. Risus commodo viverra maecenas accumsan lacus vel facilisis.</p>
</article>
<article class="abs testimonial" style="left:612px">
  <div class="avatar" role="img" aria-label="Customer portrait"></div>
  <div class="name">Donald Joe</div>
  <div class="role">CEO of joeline.com</div>
  <div class="quote">&#8221;</div>
  <p class="text">Lorem ipsum dolor sit amet, consectetur adipiscing elit, sed do eiusmod tempor incididunt ut labore et dolore magna aliqua. Quis ipsum suspendisse ultrices gravida. Risus commodo viverra maecenas accumsan lacus vel facilisis.</p>
</article>

<h2 class="section-title" style="top:1284px">Light Therapy for You &amp; Your Pets</h2>

<article class="abs card audience" style="left:201px">
  <div class="photo" style="background:linear-gradient(180deg,#4fb0c8,#3a93a8 55%,#d23030)" role="img" aria-label="Smiling man in a red sweater"></div>
  <h3 style="top:132px">People</h3>
  <p class="body" style="top:156px">Lorem ipsum dolor sit amet, consectetur adipiscing elit, sed do eiusmod tempor incididunt ut labore et dolore magna aliqua. Quis ipsum suspendisse ultrices gravida. Risus commodo viverra maecenas accumsan lacus vel</p>
  <span class="read-more" style="top:264px">READ MORE</span>
</article>
<article class="abs card audience" style="left:471px">
  <div class="photo" style="background:linear-gradient(135deg,#e8e8ec,#d9a26a 55%,#f2ede8)" role="img" aria-label="Resting shiba dog"></div>
  <h3 style="top:132px">Dogs</h3>
  <p class="body" style="top:156px">Lorem ipsum dolor sit amet, consectetur adipiscing elit, sed do eiusmod tempor incididunt ut labore et dolore magna aliqua. Quis ipsum suspendisse ultrices gravida. Risus commodo viverra maecenas accumsan lacus vel</p>
  <span class="read-more" style="top:264px">READ MORE</span>
</article>
<article class="abs card audience" style="left:743px">
  <div class="photo" style="background:linear-gradient(90deg,#2c3a2a,#cfd2cc 50%,#3a4a32)" role="img" aria-label="White horse running"></div>
  <h3 style="top:134px">Horses</h3>
  <p class="body" style="top:158px">Lorem ipsum dolor sit amet, consectetur adipiscing elit, sed do eiusmod tempor incididunt ut labore et dolore magna aliqua. Quis ipsum suspendisse ultrices gravida. Risus commodo viverra maecenas accumsan lacus vel</p>
  <span class="read-more" style="top:266px">READ MORE</span>
</article>

<section class="abs featured-band"></section>
<h2 class="section-title" style="top:1739px;color:var(--white)">Featured Products</h2>
<div class="rule light" style="top:1778px"></div>
<span class="abs arrow" style="left:200px;top:1895px">&#8249;</span>
<span class="abs arrow" style="left:993px;top:1895px">&#8250;</span>

<article class="abs product" style="left:232px">
  <div class="photo" role="img" aria-label="PBM light with charger and battery"></div>
  <div class="pname">Brivolune PBM Light w/Charger</div>
  <div class="price" style="top:140px">$599.00</div>
  <div class="view">VIEW PRODUCT</div>
</article>
<article class="abs product" style="left:420px">
  <div class="photo" role="img" aria-label="Red light with case and battery"></div>
  <div class="pname">Brivolune Red Light + Bonus</div>
  <div class="price" style="top:140px">$329.00</div>
  <div class="view">VIEW PRODUCT</div>
</article>
<article class="abs product" style="left:607px">
  <div class="photo" role="img" aria-label="Green light with case and battery"></div>
  <div class="pname">Brivolune Green Light + Bonus</div>
  <div class="price" style="top:140px">$329.00</div>
  <div class="view">VIEW PRODUCT</div>
</article>
<article class="abs product" style="left:794px">
  <div class="photo" style="background:linear-gradient(135deg,#4a3a70,#d8c0b0 55%,#e07a4a)" role="img" aria-label="Complete package with lights, case and booklets"></div>
  <div class="pname">Complete Package (People,<br>Horse,Dog)</div>
  <div class="price" style="top:152px">$399.00 – $518.00</div>
  <div class="view">VIEW PRODUCT</div>
</article>
<div class="abs dots"><span></span><span></span><span></span></div>

<h2 class="section-title" style="top:2104px">Watch the Video about the Lights</h2>
<div class="rule" style="top:2147px"></div>
<div class="abs video" role="img" aria-label="Video of two women presenting the therapy lights in a barn">
  <div class="play"><svg width="12" height="12" viewBox="0 0 12 12"><path d="M3 1l8 5-8 5z" fill="#fff"/></svg></div>
</div>

<section class="abs blog-band" role="img" aria-label="Soft meadow of pink flowers"></section>
<h2 class="section-title" style="top:2633px">Our Blog</h2>
<div class="rule" style="top:2672px"></div>

<article class="abs card post" style="left:201px">
  <div class="photo" style="background:linear-gradient(135deg,#3a2a26,#7a5a48 55%,#a02030)" role="img" aria-label="Horse tied in a stall"></div>
  <h3 style="top:138px">Best Practices - Don't Cross-Tie</h3>
  <span class="date">Jan 20, 2020</span>
  <p class="body" style="top:172px">Lorem ipsum dolor sit amet, consectetur adipiscing elit, sed do eiusmod tempor incididunt ut labore et dolore magna aliqua. Quis ipsum suspendisse ultrices gravida. Risus commodo viverra maecenas accumsan lacus vel facilisis.</p>
  <span class="read-more" style="top:282px">READ MORE</span>
</article>
<article class="abs card post" style="left:471px">
  <div class="photo" style="background:linear-gradient(135deg,#e8e8ec,#d9a26a 55%,#f2ede8)" role="img" aria-label="Resting shiba dog"></div>
  <h3 style="top:138px">Tallypoint Software on Sale!</h3>
  <span class="date">Feb 21, 2020</span>
  <p class="body" style="top:172px">Lorem ipsum dolor sit amet, consectetur adipiscing elit, sed do eiusmod tempor incididunt ut labore et dolore magna aliqua. Quis ipsum suspendisse ultrices gravida. Risus commodo viverra maecenas accumsan lacus vel</p>
  <span class="read-more" style="top:282px">READ MORE</span>
</article>
<article class="abs card post" style="left:743px">
  <div class="photo" style="background:linear-gradient(90deg,#2c3a2a,#cfd2cc 50%,#3a4a32)" role="img" aria-label="White horse running"></div>
  <h3 style="top:140px">Brivolune Light Dosing</h3>
  <span class="date" style="top:154px">Jun 9, 2019</span>
  <p class="body" style="top:174px">Lorem ipsum dolor sit amet, consectetur adipiscing elit, sed do eiusmod tempor incididunt ut labore et dolore magna aliqua. Quis ipsum suspendisse ultrices gravida. Risus commodo viverra maecenas accumsan lacus vel</p>
  <span class="read-more" style="top:284px">READ MORE</span>
</article>

<h2 class="section-title" style="top:3064px">STAY UP TO DATE</h2>
<div class="rule" style="top:3106px"></div>
<p class="abs" style="left:0;top:3128px;width:1200px;text-align:center;font-size:10.5px">Get notified about the newest products and upcoming sales</p>
<div class="abs signup-field" style="top:3183px">Name</div>
<div class="abs signup-field" style="top:3230px">Email</div>
<span class="abs btn" style="left:440px;top:3276px;width:321px;height:40px;font-size:10px">SUBSCRIBE</span>

<footer class="abs footer">
  <div class="brand"><span class="dot"></span>Brivolune</div>
  <small style="left:370px;top:36px">Search here</small>
  <span class="abs" style="left:370px;top:52px;width:160px;height:22px;background:var(--white)"></span>
  <span class="abs" style="left:530px;top:52px;width:48px;height:22px;background:#e6e6e6;color:#555;font-size:8px;display:flex;align-items:center;justify-content:center">Search</span>
  <div class="links">Lifetime Product Warranty<br>No-Worries Guarantee<br>Disclaimer<br>Terms of Use<br>GDPR Privacy Policy</div>
  <small style="left:851px;top:37px">Distributor Registration &amp; Login</small>
</footer>

</body>
</html>
```